Dorvelan Swimming & Athletics Center

We need Business Card for a Athletics center
The logo frome the Uploaded Files ( b card fimal)
Οn one side of card we need the logo of company the Contact and the website:
1. Address:(Limassol, Cyprus 12-14 Stavrinelou str,Ano Trimeni,P.C. 4832)

2.Phone number: (+357) 25-704263

3. Mail: info@dorvelanfit.example

3. Website: www.dorvelanfit.example

Οn the other side of the card we need to write the sport of the company:

1. Artistic Gymnastics
2. Swimming
3. Gym - Fitness
4. Programs
5. Dancing
5.Tennis

From the Uploaded Files you can get the logo.In a logo is behind the black color which can be removed from logo.

Υou can use that color you want.
.
Updates

Industry/Entity Type

Business

Font styles to use
Decorative

Colors
0555a3
ffcf3e
3176b5
0692cd
add136
f04a50
000000
cfcfcf
9d9d9d

Requirements
Should not have
• photos with faces
• photo fro the Website:www.dorvelanfit.example

```html
<!DOCTYPE html>
<html lang="en">
<head>
<meta charset="utf-8">
<title>Dorvelan Swimming &amp; Athletics Center – Business Card</title>
<link rel="stylesheet" href="https://fonts.googleapis.com/css2?family=Oswald:wght@300;400;700&display=swap">
<style>
  :root {
    --navy: #0555a3;
    --gold: #ffcf3e;
    --blue: #3176b5;
    --sky: #0692cd;
    --lime: #add136;
    --coral: #f04a50;
    --black: #000000;
    --silver: #cfcfcf;
    --grey: #9d9d9d;
    --paper: #ffffff;
    --stage: #eebd2c;
  }
  * { margin: 0; padding: 0; box-sizing: border-box; }
  html, body { width: 1200px; height: 1200px; overflow: hidden; }
  body {
    background: var(--stage);
    font-family: "Oswald", sans-serif;
    display: flex;
    flex-direction: column;
    align-items: center;
    justify-content: center;
    gap: 52px;
  }
  .card {
    position: relative;
    width: 900px;
    height: 514px;
    overflow: hidden;
    box-shadow: 0 6px 18px rgba(0,0,0,0.18);
  }
  /* front */
  .card--front { background: var(--black); color: var(--paper); }
  .edge-strip {
    position: absolute;
    display: flex;
  }
  .edge-strip span { flex: 1; }
  .edge-strip .c1 { background: var(--lime); }
  .edge-strip .c2 { background: var(--sky); }
  .edge-strip .c3 { background: var(--gold); }
  .edge-strip .c4 { background: var(--grey); }
  .edge-strip .c5 { background: var(--coral); }
  .edge-strip--bottom { left: 0; right: 0; bottom: 0; height: 10px; }
  .edge-strip--left, .edge-strip--right { top: 0; bottom: 0; width: 10px; flex-direction: column; }
  .edge-strip--left { left: 0; }
  .edge-strip--right { right: 0; }

  .brand {
    position: absolute;
    left: 150px;
    top: 128px;
    display: flex;
    align-items: center;
    gap: 34px;
  }
  .brand-name {
    font-weight: 700;
    font-size: 112px;
    line-height: 1;
    letter-spacing: 4px;
    color: var(--gold);
  }
  .brand-mark {
    width: 112px;
    height: 112px;
    border-radius: 50%;
    border: 4px solid var(--gold);
  }
  .rule {
    position: absolute;
    height: 1px;
    background: var(--grey);
  }
  .rule--upper { left: 380px; right: 40px; top: 282px; }
  .rule--lower { left: 70px; right: 200px; top: 352px; }
  .website {
    position: absolute;
    left: 0; right: 0; top: 298px;
    text-align: center;
    font-weight: 300;
    font-size: 22px;
    letter-spacing: 1.5px;
  }
  .contact {
    position: absolute;
    top: 370px;
    left: 70px;
    right: 40px;
    font-weight: 300;
    font-size: 21px;
    line-height: 1.55;
  }
  .contact .label { color: var(--gold); font-weight: 400; margin-right: 6px; }
  .contact .indent { padding-left: 290px; }

  /* back */
  .card--back { background: var(--paper); }
  .card--back svg { position: absolute; inset: 0; }
  .sport-label {
    font-family: "Oswald", sans-serif;
    font-weight: 300;
    font-size: 24px;
    letter-spacing: 1.5px;
    fill: var(--paper);
  }
</style>
</head>
<body>

<section class="card card--front" aria-label="Business card front">
  <div class="brand">
    <span class="brand-name">DORVELAN</span>
    <span class="brand-mark" aria-hidden="true"></span>
  </div>
  <div class="rule rule--upper"></div>
  <p class="website">www.dorvelanfit.example</p>
  <div class="rule rule--lower"></div>
  <div class="contact">
    <p><span class="label">A:</span>Limassol, Cyprus 12-14 Stavrinelou str, Ano Trimeni, P.C. 4832</p>
    <p class="indent"><span class="label">P:</span>(+357) 25-704263</p>
    <p class="indent"><span class="label">M:</span>info@dorvelanfit.example</p>
  </div>
  <div class="edge-strip edge-strip--bottom"><span class="c1"></span><span class="c2"></span><span class="c3"></span><span class="c4"></span><span class="c5"></span></div>
</section>

<section class="card card--back" aria-label="Business card back">
  <svg width="900" height="514" viewBox="0 0 900 514">
    <circle cx="470" cy="270" r="200" fill="none" stroke="#ececec" stroke-width="14"/>
    <g class="sport-rows" stroke="#000" stroke-width="3">
      <g transform="translate(0,0)">
        <line x1="100" y1="130" x2="620" y2="130"/>
        <rect x="270" y="94" width="340" height="36" fill="#000"/>
        <line x1="258" y1="86" x2="258" y2="134"/><line x1="622" y1="86" x2="622" y2="134"/>
        <text class="sport-label" x="440" y="121" text-anchor="middle" stroke="none">Artistic Gymnastics</text>
      </g>
      <g transform="translate(40,62)">
        <line x1="100" y1="130" x2="620" y2="130"/>
        <rect x="270" y="94" width="340" height="36" fill="#000"/>
        <line x1="258" y1="86" x2="258" y2="134"/><line x1="622" y1="86" x2="622" y2="134"/>
        <text class="sport-label" x="440" y="121" text-anchor="middle" stroke="none">Swimming</text>
      </g>
      <g transform="translate(80,124)">
        <line x1="100" y1="130" x2="620" y2="130"/>
        <rect x="270" y="94" width="340" height="36" fill="#000"/>
        <line x1="258" y1="86" x2="258" y2="134"/><line x1="622" y1="86" x2="622" y2="134"/>
        <text class="sport-label" x="440" y="121" text-anchor="middle" stroke="none">Gym - Fitness</text>
      </g>
      <g transform="translate(120,186)">
        <line x1="100" y1="130" x2="620" y2="130"/>
        <rect x="270" y="94" width="340" height="36" fill="#000"/>
        <line x1="258" y1="86" x2="258" y2="134"/><line x1="622" y1="86" x2="622" y2="134"/>
        <text class="sport-label" x="440" y="121" text-anchor="middle" stroke="none">Programs</text>
      </g>
      <g transform="translate(160,248)">
        <line x1="100" y1="130" x2="620" y2="130"/>
        <rect x="270" y="94" width="340" height="36" fill="#000"/>
        <line x1="258" y1="86" x2="258" y2="134"/><line x1="622" y1="86" x2="622" y2="134"/>
        <text class="sport-label" x="440" y="121" text-anchor="middle" stroke="none">Dancing</text>
      </g>
      <g transform="translate(200,310)">
        <line x1="20" y1="130" x2="500" y2="130"/>
        <rect x="270" y="94" width="340" height="36" fill="#000"/>
        <line x1="258" y1="86" x2="258" y2="134"/><line x1="622" y1="86" x2="622" y2="134"/>
        <text class="sport-label" x="440" y="121" text-anchor="middle" stroke="none">Tennis</text>
      </g>
    </g>
  </svg>
  <div class="edge-strip edge-strip--left"><span class="c1"></span><span class="c2"></span><span class="c3"></span><span class="c4"></span><span class="c5"></span></div>
  <div class="edge-strip edge-strip--right"><span class="c1"></span><span class="c2"></span><span class="c3"></span><span class="c4"></span><span class="c5"></span></div>
</section>

</body>
</html>
```